K.T.L Electrical Services Pty Ltd

Electrical contracting business. I have a base for the design which i like. The contact number needs to be changed to 0491736250 and the O made more solid and level with the rest of the letters. If you have any other ideas of what would make it better I'm happy to see them.

The back side to be written as dot points with the following:
- Residential & Commercial
- Maintenance
- PV & Battery servicing
- EV Chargers

```html
<!DOCTYPE html>
<html lang="en">
<head>
<meta charset="utf-8">
<title>K.T.L Electrical Services – Business Card</title>
<link rel="stylesheet" href="https://fonts.googleapis.com/css2?family=Montserrat:wght@500;600;800&display=swap">
<style>
  :root {
    --bg: #2c2c2c;
    --card: #1b1b1b;
    --teal: #8fb0b4;
    --copper: #c98a55;
  }
  * { margin: 0; padding: 0; box-sizing: border-box; }
  html, body {
    width: 1200px; height: 689px; overflow: hidden;
    background: var(--bg);
    font-family: "Montserrat", Arial, sans-serif;
  }
  .card {
    position: absolute; top: 190px;
    width: 530px; height: 310px;
    background: var(--card);
    border-radius: 18px;
    box-shadow: 0 12px 30px rgba(0,0,0,.45);
    overflow: hidden;
  }
  .card--back { left: 40px; }
  .card--front { left: 630px; }

  /* back */
  .services { list-style: none; position: absolute; left: 58px; top: 62px; }
  .services__item {
    display: flex; align-items: center; gap: 16px;
    color: var(--teal); font-weight: 500; font-size: 23px;
    letter-spacing: 1.5px; text-transform: uppercase;
    height: 40px;
  }
  .services__bolt { width: 12px; height: 20px; flex: none; }
  .rule { position: absolute; height: 1px; background: var(--teal); }
  .card--back .rule { left: 0; right: 40px; bottom: 46px; }
  .rule__end {
    position: absolute; right: 30px; bottom: 41px;
    width: 11px; height: 11px; border: 1px solid var(--teal); border-radius: 50%;
  }

  /* front */
  .brand { position: absolute; left: 78px; top: 44px; color: var(--teal); font-weight: 600; }
  .brand__row { display: flex; align-items: center; gap: 18px; }
  .brand__dot { width: 58px; height: 58px; border-radius: 50%; background: var(--teal); }
  .brand__initials { font-size: 80px; line-height: 1; letter-spacing: 4px; }
  .brand__tagline { font-size: 17px; letter-spacing: 6px; margin-top: 12px; }
  .licence {
    position: absolute; left: 78px; top: 172px;
    color: var(--copper); font-size: 15px; font-weight: 500; letter-spacing: 1.5px;
  }
  .card--front .rule { left: 78px; right: 40px; top: 204px; }
  .card--front .rule__end { top: 199px; bottom: auto; }
  .contact {
    position: absolute; left: 40px; right: 40px; bottom: 30px; height: 56px;
    border: 1px solid var(--teal); border-radius: 12px;
    display: flex; align-items: center; gap: 18px; padding-left: 140px;
  }
  .contact__icon { width: 34px; height: 34px; }
  .contact__number {
    color: var(--teal); font-weight: 800; font-size: 30px; letter-spacing: 2px;
  }
</style>
</head>
<body>

<section class="card card--back">
  <ul class="services">
    <li class="services__item"><svg class="services__bolt" viewBox="0 0 12 20"><polygon points="8,0 1,11 6,11 3,20 11,8 6,8" fill="#c98a55"/></svg>Residential &amp; Commercial</li>
    <li class="services__item"><svg class="services__bolt" viewBox="0 0 12 20"><polygon points="8,0 1,11 6,11 3,20 11,8 6,8" fill="#c98a55"/></svg>Maintenance</li>
    <li class="services__item"><svg class="services__bolt" viewBox="0 0 12 20"><polygon points="8,0 1,11 6,11 3,20 11,8 6,8" fill="#c98a55"/></svg>PV &amp; Battery Servicing</li>
    <li class="services__item"><svg class="services__bolt" viewBox="0 0 12 20"><polygon points="8,0 1,11 6,11 3,20 11,8 6,8" fill="#c98a55"/></svg>EV Chargers</li>
  </ul>
  <div class="rule"></div>
  <div class="rule__end"></div>
</section>

<section class="card card--front">
  <div class="brand">
    <div class="brand__row">
      <span class="brand__dot"></span>
      <span class="brand__initials">K.T.L</span>
    </div>
    <div class="brand__tagline">ELECTRICAL SERVICES P/L</div>
  </div>
  <div class="licence">EC20417</div>
  <div class="rule"></div>
  <div class="rule__end"></div>
  <div class="contact">
    <svg class="contact__icon" viewBox="0 0 34 34">
      <circle cx="17" cy="17" r="15.5" fill="none" stroke="#c98a55" stroke-width="1.5"/>
      <path d="M11 13c0 6 4 10 10 10l2-3-3-2-2 1.5c-1.5-.8-3-2.3-3.7-3.8L16 14l-2-3z" fill="#c98a55"/>
    </svg>
    <span class="contact__number">0491736250</span>
  </div>
</section>

</body>
</html>
```